Fun Language School in San Diego, CA - We want cool Business Card

We need a new business card design for our new logo. We are a language school in beautiful San Diego, California. Our target is students from all over the world who age from 18 to 25. They come to our school to learn English. Our school has a modern look, trending and fun place. We are the only language school who use tablets in class. We are student oriented, Students Come First is our slogan. We are re-branding ourselves with a new logo. We would like to see a designs that use our new logo and it should reflect the feel of young, fun, modern, high-tech and attractive to young people.
I've seen some business card designs with transparent look, unusual shapes, we are open to any cool ideas. Thank you very much!

In order for you to know more about our school, here are the links to our Youtube Channel and Facebook.

Youtube: https://www.vidmarlo.example/channel/ZXpolrT-48kwb2nH7c5DqLm
Facebook: https://www.friendlane.example/BVSchool

Target Market(s)

Our target is students from all over the world who age from 18 to 25. International students.

Industry/Entity Type

School

Font styles to use
Sans Serif

Requirements
Must have
• Our new logo. Name, title and address.
Should not have
• Other colors other than the ones we have in our logo. Characters are fine.

```html
<!DOCTYPE html>
<html lang="en">
<head>
<meta charset="utf-8">
<title>BVSchool Business Card</title>
<link rel="stylesheet" href="https://fonts.googleapis.com/css2?family=Quicksand:wght@400;500;700&display=swap">
<style>
  :root {
    --blue: #4f9ccb;
    --lime: #c5d62e;
    --teal: #6cbfb4;
    --grey: #6d6e71;
    --ink: #333333;
    --paper: #ffffff;
    --table: #d7d8da;
  }
  * { box-sizing: border-box; margin: 0; padding: 0; }
  html, body {
    width: 1200px;
    height: 772px;
    overflow: hidden;
    background: var(--table);
    font-family: "Quicksand", sans-serif;
  }
  .stage {
    position: relative;
    width: 1200px;
    height: 772px;
    display: flex;
    align-items: center;
    justify-content: center;
    gap: 60px;
  }
  .card {
    position: relative;
    width: 540px;
    height: 309px;
    background: var(--paper);
    overflow: hidden;
    box-shadow: 0 6px 18px rgba(0,0,0,0.18);
  }
  .card__art {
    position: absolute;
    inset: 0;
    width: 100%;
    height: 100%;
  }
  .brand {
    position: absolute;
    display: flex;
    align-items: center;
    gap: 12px;
    color: var(--grey);
    font-weight: 500;
  }
  .brand__dot {
    border-radius: 50%;
    background: var(--teal);
  }
  .card--front .brand { top: 26px; left: 30px; font-size: 28px; }
  .card--front .brand__dot { width: 36px; height: 36px; }
  .card--back .brand {
    top: 50%; left: 50%;
    transform: translate(-50%, -50%);
    font-size: 46px;
  }
  .card--back .brand__dot { width: 58px; height: 58px; }

  .address {
    position: absolute;
    top: 34px;
    right: 28px;
    text-align: right;
    font-size: 14px;
    font-style: normal;
    line-height: 1.45;
    color: var(--ink);
    font-weight: 500;
  }
  .contacts {
    position: absolute;
    top: 120px;
    right: 24px;
    width: 176px;
    list-style: none;
    font-size: 13px;
    color: var(--ink);
    font-weight: 500;
  }
  .contacts li {
    display: flex;
    align-items: center;
    gap: 9px;
    height: 22px;
    white-space: nowrap;
  }
  .contacts svg { width: 13px; height: 13px; flex: none; }
  .person {
    position: absolute;
    left: 32px;
    bottom: 26px;
    color: var(--paper);
  }
  .person__name {
    font-size: 17px;
    font-weight: 700;
    letter-spacing: 1.5px;
    text-transform: uppercase;
  }
  .person__role {
    font-size: 13px;
    font-weight: 500;
    margin-top: 2px;
  }
</style>
</head>
<body>
<main class="stage">

  <section class="card card--front" aria-label="Business card front">
    <svg class="card__art" viewBox="0 0 540 309" preserveAspectRatio="none" aria-hidden="true">
      <path d="M0,82 C140,110 265,190 330,309" fill="none" stroke="var(--lime)" stroke-width="9"/>
      <path d="M0,132 C130,158 225,222 282,309 L0,309 Z" fill="var(--blue)"/>
    </svg>

    <div class="brand"><span class="brand__dot"></span><span class="brand__name">BVSchool</span></div>

    <address class="address">
      214 Harbor View Ave<br>San Diego CA
    </address>

    <ul class="contacts">
      <li>
        <svg viewBox="0 0 16 16"><path d="M4 1 L6.5 4 L5 6 C6 8.5 7.5 10 10 11 L12 9.5 L15 12 L13 15 C7 14.5 1.5 9 1 3 Z" fill="#333"/></svg>
        619 555 0142
      </li>
      <li>
        <svg viewBox="0 0 16 16"><rect x="4" y="1" width="8" height="14" rx="1.5" fill="none" stroke="#333" stroke-width="1.6"/><circle cx="8" cy="12.5" r="1" fill="#333"/></svg>
        619 555 0143
      </li>
      <li>
        <svg viewBox="0 0 16 16"><rect x="1" y="6" width="14" height="8" rx="1" fill="#333"/><rect x="4" y="1" width="8" height="5" fill="none" stroke="#333" stroke-width="1.4"/></svg>
        619 555 0144
      </li>
      <li>
        <svg viewBox="0 0 16 16"><circle cx="8" cy="8" r="6.5" fill="none" stroke="#333" stroke-width="1.4"/><ellipse cx="8" cy="8" rx="3" ry="6.5" fill="none" stroke="#333" stroke-width="1.2"/><path d="M1.5 8 H14.5" stroke="#333" stroke-width="1.2"/></svg>
        maya@bvschool.example
      </li>
      <li>
        <svg viewBox="0 0 16 16"><circle cx="8" cy="8" r="6.5" fill="none" stroke="#333" stroke-width="1.4"/><path d="M5 8 H11 M8 5 L11 8 L8 11" fill="none" stroke="#333" stroke-width="1.4"/></svg>
        www.bvschool.example
      </li>
    </ul>

    <div class="person">
      <p class="person__name">Maya Torres</p>
      <p class="person__role">Managing Director</p>
    </div>
  </section>

  <section class="card card--back" aria-label="Business card back">
    <div class="brand"><span class="brand__dot"></span><span class="brand__name">BVSchool</span></div>
  </section>

</main>
</body>
</html>
```